Need Letterhead Design & Matching Business Card

I have a logo that I love already. But the letterhead is less than appealing and boring. I'd like a design for my letterhead which I will match with business cards. Also, I'd like to have used fonts that are generally available, as my current letterhead uses a font named "SPACE" which nobody has unless they download it...so when a Word version is forwarded, it looks awful on the receiver's screed due to not having the font. That being said, modern is the look we like and are going for.

My business is "Halloran Brightmoor PC" - a law firm specializing in representing people who have suffered catastrophic injuries or death (plane, auto, train crashes etc.).

See attached letterhead, which has all of the pertinent information. My logo is also attached in various formats.

```html
<!DOCTYPE html>
<html lang="en">
<head>
<meta charset="UTF-8">
<title>Halloran Brightmoor PC – Stationery</title>
<link href="https://fonts.googleapis.com/css2?family=Inter:wght@300;400;600&display=swap" rel="stylesheet">
<style>
  :root {
    --backdrop: #d9d9d9;
    --paper: #fbfbfb;
    --ink: #1f1f1f;
    --ink-soft: #5a5a5a;
    --rule: #9a9a9a;
    --mark: #2b2b2b;
    --sign: #c9cfe0;
    --shadow: 0 6px 18px rgba(0,0,0,.12);
  }
  * { box-sizing: border-box; margin: 0; padding: 0; }
  html, body { width: 1200px; height: 900px; overflow: hidden; }
  body {
    background: var(--backdrop);
    font-family: "Inter", Arial, sans-serif;
    color: var(--ink);
    position: relative;
  }
  .sheet { position: absolute; background: var(--paper); box-shadow: var(--shadow); }
  .brand-square { display: inline-block; background: var(--mark); flex: none; }
  .wordmark { font-weight: 300; text-transform: uppercase; letter-spacing: .04em; line-height: 1.05; }

  /* Letterhead */
  .letterhead { left: 70px; top: 115px; width: 470px; height: 665px; padding: 40px 40px 30px; display: flex; flex-direction: column; }
  .letterhead__header { display: flex; justify-content: space-between; align-items: flex-start; padding-bottom: 14px; border-bottom: 1px solid var(--rule); }
  .letterhead__header .wordmark { font-size: 22px; }
  .letterhead__header .brand-square { width: 34px; height: 34px; }
  .letter { font-size: 7px; line-height: 1.55; color: var(--ink-soft); padding-top: 22px; flex: 1; }
  .letter__recipient { margin-bottom: 14px; }
  .letter__salutation { font-weight: 600; color: var(--ink); margin-bottom: 8px; }
  .letter p { margin-bottom: 8px; }
  .letter__closing { margin-top: 14px; }
  .letter__signature { width: 80px; height: 22px; background: var(--sign); margin: 6px 0; border-radius: 3px; }
  .letter__signer { font-weight: 600; color: var(--ink); }
  .letterhead__footer { border-top: 1px solid var(--rule); padding-top: 10px; display: flex; justify-content: space-between; font-size: 6px; line-height: 1.5; color: var(--ink-soft); white-space: nowrap; }
  .letterhead__footer div { padding-left: 8px; border-left: 1px solid var(--rule); }
  .letterhead__footer div:first-child { border-left: 0; padding-left: 0; }
  .letterhead__footer strong { color: var(--ink); font-weight: 600; }

  /* Envelope front */
  .envelope { left: 600px; width: 530px; height: 230px; }
  .envelope--front { top: 115px; padding: 24px; }
  .envelope--front .wordmark { font-size: 13px; }
  .envelope__address { font-size: 6.5px; line-height: 1.5; color: var(--ink-soft); margin-top: 6px; }

  /* Envelope back */
  .envelope--back { top: 380px; }
  .envelope--back svg { position: absolute; inset: 0; }
  .envelope__seal { position: absolute; left: 50%; top: 104px; transform: translateX(-50%); display: flex; align-items: center; gap: 6px; font-size: 8px; white-space: nowrap; }
  .envelope__seal .brand-square { width: 14px; height: 14px; }

  /* Business cards */
  .card { top: 640px; width: 255px; height: 146px; }
  .card--brand { left: 600px; display: flex; align-items: center; justify-content: center; gap: 12px; }
  .card--brand .brand-square { width: 30px; height: 30px; }
  .card--brand .wordmark { font-size: 15px; }
  .card--contact { left: 875px; padding: 16px 18px; }
  .card--contact .wordmark { font-size: 12px; }
  .card__person { font-size: 6.5px; line-height: 1.5; color: var(--ink-soft); margin-top: 10px; }
  .card__person strong { color: var(--ink); font-weight: 600; }
  .card__foot { position: absolute; left: 18px; right: 18px; bottom: 14px; display: flex; justify-content: space-between; align-items: flex-end; }
  .card__foot .brand-square { width: 22px; height: 22px; }
  .card__office { font-size: 6px; line-height: 1.5; color: var(--ink-soft); text-align: right; white-space: nowrap; }
</style>
</head>
<body>

<section class="sheet letterhead">
  <header class="letterhead__header">
    <div class="wordmark">Halloran<br>Brightmoor PC</div>
    <span class="brand-square"></span>
  </header>

  <article class="letter">
    <div class="letter__recipient">
      Mr. Martin Ellery<br>
      President and CEO<br>
      Northfield Works LLC<br>
      220 Mercer Lane, Suite 310<br>
      Ashford, NY 12840
    </div>
    <div class="letter__salutation">Dear Mr. Ellery,</div>
    <p>As Chairperson of the Community Relief Campaign, I am writing to thank you personally for your company's support in this year's fund-raising effort. The campaign was a clear success.</p>
    <p>Your team raised far more than we had hoped, well beyond the target we set at the start. We could not have reached this result without your steady help and generous spirit.</p>
    <p>I would also like to thank every person in your company who gave time to the cause. Please pass on our warm thanks to all of them.</p>
    <p>I believe the firms that took part have set a new standard for service in this community, and I look forward to seeing you at the reception next month.</p>
    <div class="letter__closing">Yours sincerely,</div>
    <div class="letter__signature" role="img" aria-label="Handwritten signature"></div>
    <div class="letter__signer">Peter Lindqvist</div>
    <div>Fundraising Chair</div>
  </article>

  <footer class="letterhead__footer">
    <div><strong>Halloran Brightmoor PC</strong><br>www.halloranbrightmoor.com</div>
    <div><strong>R. Daniel Okafor</strong>, Esq.<br>President</div>
    <div>4400 Harbor Crest Ave.<br>Suite 620, Westlake, CA 93017</div>
    <div>T: (555) 010-4821<br>E: dan@halloranbrightmoor.com</div>
  </footer>
</section>

<section class="sheet envelope envelope--front">
  <div class="wordmark">Halloran<br>Brightmoor PC</div>
  <div class="envelope__address">4400 Harbor Crest Ave., Suite 620<br>Westlake, CA 93017</div>
</section>

<section class="sheet envelope envelope--back">
  <svg width="530" height="230" viewBox="0 0 530 230" aria-hidden="true">
    <path d="M0 0 L265 130 L530 0" fill="none" stroke="#cfcfcf" stroke-width="1"/>
    <path d="M0 230 L220 110 M530 230 L310 110" fill="none" stroke="#e2e2e2" stroke-width="1"/>
  </svg>
  <div class="envelope__seal">
    <span class="brand-square"></span>
    <span class="wordmark">Halloran Brightmoor PC</span>
  </div>
</section>

<section class="sheet card card--brand">
  <span class="brand-square"></span>
  <div class="wordmark">Halloran<br>Brightmoor PC</div>
</section>

<section class="sheet card card--contact">
  <div class="wordmark">Halloran<br>Brightmoor PC</div>
  <div class="card__person">
    <strong>R. Daniel Okafor</strong>, Esq.<br>
    President<br>
    T: (555) 010-4821<br>
    E: dan@halloranbrightmoor.com
  </div>
  <div class="card__foot">
    <div class="card__office">Halloran Brightmoor PC<br>4400 Harbor Crest Ave., Suite 620<br>Westlake, CA 93017</div>
    <span class="brand-square"></span>
  </div>
</section>

</body>
</html>
```